Skin Care Branding / Package design

We are a manufacturer of consumable hemp products and have some skin care products we want to group into a brand of its own, under our primary brand which is TurnLo.  our website is www.turnloco-example.com
Our current packaging was developed on the fly with little or no thought given to a sub brand concept.  We have sub branded other products such as Quiet Arc, Moss Lantern, and Flagon.  While Turnlo appears on the packaging it is not the predominate brand.
The products will be sold in cosmetic stores, health stores, medspas, pharmacies and other upscale stores.  We want the appeal to be elegant & upscale and stand out on the shelf.
We are open to changing the jar, bottle or container and look forward to any recommendations on this.
Later we will need flyers, social media ads, and other graphics.
Our primary goal is to create designs for each of our products that are consistent and create another sub brand.
We are also open to changing the names of these products.
images of the existing products are attached, we plan to add more skin care products.

```html
<!DOCTYPE html>
<html lang="en">
<head>
<meta charset="utf-8">
<title>TurnLo Skin Care – Label System</title>
<link rel="stylesheet" href="https://fonts.googleapis.com/css2?family=Roboto:wght@400;500;700&display=swap">
<style>
  :root {
    --backdrop: #b3b3b3;
    --white: #ffffff;
    --ink: #1e1e1e;
    --ink-soft: #3a3a3a;
    --rule: #bbbbbb;
    --orange: #e6834f;
    --teal: #62bcbd;
    --lavender: #a896c9;
    --forest: #2f5a3b;
    --mauve: #8c7d83;
    --mauve-light: #cdc3c7;
  }
  * { box-sizing: border-box; margin: 0; padding: 0; }
  html, body { width: 1200px; height: 800px; overflow: hidden; }
  body {
    background: var(--backdrop);
    font-family: "Roboto", Arial, sans-serif;
    color: var(--ink);
    position: relative;
  }

  .label {
    position: absolute;
    background: var(--tone);
    display: flex;
    flex-direction: column;
    align-items: center;
  }
  .brand-name {
    color: var(--white);
    font-weight: 700;
    letter-spacing: 0.04em;
    line-height: 1;
    display: flex;
    align-items: center;
  }
  .title-box {
    background: var(--white);
    width: 92%;
    padding: 4px 6px;
  }
  .title-box .product { font-weight: 700; line-height: 1.05; }
  .title-box .sub { font-weight: 400; color: var(--ink-soft); line-height: 1.1; }
  .info-box {
    background: var(--white);
    width: 92%;
    display: flex;
    align-items: center;
    gap: 6px;
    padding: 6px;
  }
  .badge {
    background: var(--tone);
    color: var(--white);
    border-radius: 0 50% 50% 50%;
    display: flex;
    flex-direction: column;
    align-items: center;
    justify-content: center;
    text-align: center;
    font-weight: 500;
    line-height: 1.05;
    flex: none;
  }
  .badge small { display: block; }
  .dose { text-align: center; color: var(--ink-soft); flex: 1; }
  .dose .line { border-bottom: 1px solid var(--rule); padding-bottom: 2px; margin-bottom: 2px; }
  .net-wt { color: var(--white); font-size: 6px; letter-spacing: 0.03em; }
  .claims { font-size: 7px; letter-spacing: 0.2em; color: var(--ink-soft); }

  /* Glide roll-on */
  .roll-on { --tone: var(--orange); width: 106px; height: 176px; top: 528px; padding-top: 10px; }
  .roll-on.first { left: 47px; }
  .roll-on.second { left: 195px; }
  .roll-on .brand-name { font-size: 15px; height: 48px; }
  .roll-on .product { font-size: 11px; }
  .roll-on .sub { font-size: 7.5px; }
  .roll-on .info-box { margin-top: 6px; height: 64px; }
  .roll-on .badge { width: 38px; height: 38px; font-size: 6.5px; }
  .roll-on .dose { font-size: 6px; }
  .roll-on .net-wt { margin-top: 8px; font-size: 5px; }

  /* Facial serum */
  .serum { --tone: var(--teal); left: 341px; top: 469px; width: 129px; height: 235px; padding-top: 22px; }
  .serum .brand-name { font-size: 20px; height: 62px; }
  .serum .product { font-size: 14px; }
  .serum .sub { font-size: 9px; }
  .serum .info-box { margin-top: 6px; height: 76px; flex-wrap: wrap; justify-content: center; }
  .serum .badge { width: 44px; height: 44px; font-size: 13px; }
  .serum .badge small { font-size: 6.5px; }
  .serum .dose { font-size: 9px; }
  .serum .claims { width: 100%; text-align: center; font-size: 5.5px; letter-spacing: 0.15em; }
  .serum .net-wt { margin-top: 8px; }

  /* Calming lotion */
  .lotion { --tone: var(--lavender); left: 517px; top: 449px; width: 136px; height: 224px; padding-top: 22px; }
  .lotion .brand-name { font-size: 20px; height: 64px; }
  .lotion .product { font-size: 14px; }
  .lotion .sub { font-size: 9px; }
  .lotion .info-box { margin-top: 6px; height: 76px; flex-wrap: wrap; justify-content: center; }
  .lotion .badge { width: 44px; height: 44px; font-size: 11px; }
  .lotion .dose { font-size: 8.5px; }
  .lotion .claims { width: 100%; text-align: center; font-size: 5.5px; letter-spacing: 0.05em; color: var(--ink); }
  .lotion .net-wt { margin-top: 8px; }

  /* Wide jar labels */
  .jar { flex-direction: row; align-items: stretch; padding: 10px; gap: 8px; }
  .jar .brand-side { display: flex; align-items: center; justify-content: center; flex: 1; }
  .jar .panel { background: var(--white); display: flex; flex-direction: column; padding: 6px 8px; }
  .jar .net-wt { position: absolute; bottom: 4px; left: 0; right: 0; text-align: center; }

  .muscle { --tone: var(--forest); left: 677px; top: 630px; width: 216px; height: 88px; padding-bottom: 16px; }
  .muscle .brand-name { font-size: 15px; }
  .muscle .panel { width: 102px; }
  .muscle .product { font-size: 9.5px; font-weight: 700; }
  .muscle .sub { font-size: 7.5px; color: var(--ink-soft); }
  .muscle .row { display: flex; align-items: center; gap: 4px; margin-top: 4px; }
  .muscle .badge { width: 28px; height: 28px; font-size: 7px; }
  .muscle .dose { font-size: 9px; }
  .muscle .dose small { font-size: 6px; }

  .vitamin { --tone: var(--mauve); background: linear-gradient(180deg, var(--mauve-light), var(--mauve)); left: 915px; top: 612px; width: 230px; height: 108px; padding-bottom: 16px; }
  .vitamin .brand-name { font-size: 15px; }
  .vitamin .panel { width: 138px; }
  .vitamin .product { font-size: 13px; font-weight: 700; line-height: 1; }
  .vitamin .sub { font-size: 11px; line-height: 1; }
  .vitamin .row { display: flex; align-items: center; gap: 6px; margin-top: 3px; }
  .vitamin .badge { width: 44px; height: 44px; font-size: 13px; }
  .vitamin .badge small { font-size: 6px; }
  .vitamin .dose { font-size: 8px; }
  .vitamin .dose small { font-size: 6px; display: block; }
  .vitamin .claims { font-size: 5.5px; letter-spacing: 0.12em; margin-top: 2px; }
</style>
</head>
<body>

  <section class="label roll-on first">
    <div class="brand-name">TurnLo</div>
    <div class="title-box"><p class="product">Glide</p><p class="sub">Gel Muscle Roll-On</p></div>
    <div class="info-box">
      <div class="badge">CANNA-<br>BINIODS</div>
      <div class="dose"><p class="line">50/50 Blend Of</p><p>6000 MG</p></div>
    </div>
    <p class="net-wt">NET WT 3 OZ / 90G</p>
  </section>

  <section class="label roll-on second">
    <div class="brand-name">TurnLo</div>
    <div class="title-box"><p class="product">Glide</p><p class="sub">Gel Muscle Roll-On</p></div>
    <div class="info-box">
      <div class="badge">CANNA-<br>BINIODS</div>
      <div class="dose"><p class="line">50/50 Blend Of</p><p>6000 MG</p></div>
    </div>
    <p class="net-wt">NET WT 3 OZ / 90G</p>
  </section>

  <section class="label serum">
    <div class="brand-name">TurnLo</div>
    <div class="title-box"><p class="product">Facial Serum</p><p class="sub">For Beauty</p></div>
    <div class="info-box">
      <div class="badge">CBG<small>INFUSED</small></div>
      <div class="dose"><p class="line">300mg CBG</p></div>
      <p class="claims">TONE | HYDRATE | SOFTEN</p>
    </div>
    <p class="net-wt">NET WT .5 OZ / 15G</p>
  </section>

  <section class="label lotion">
    <div class="brand-name">TurnLo</div>
    <div class="title-box"><p class="product">Calming</p><p class="sub">Lavander Lotion</p></div>
    <div class="info-box">
      <div class="badge">CBD<br>+<br>CBG</div>
      <div class="dose"><p class="line">50/50 Blend</p><p>800mg</p></div>
      <p class="claims">INFUSED DAILY MOISTURIZER</p>
    </div>
    <p class="net-wt">4fl oz / 120 ml</p>
  </section>

  <section class="label jar muscle">
    <div class="brand-side"><div class="brand-name">TurnLo</div></div>
    <div class="panel">
      <p class="product">Muscle &amp; Joint</p>
      <p class="sub">Cream</p>
      <div class="row">
        <div class="badge">CBD<br>+<br>CBG</div>
        <div class="dose"><p class="line">1500mg</p><small>Full Spectrum</small></div>
      </div>
    </div>
    <p class="net-wt">NET WT 1 OZ / 30G</p>
  </section>

  <section class="label jar vitamin">
    <div class="brand-side"><div class="brand-name">TurnLo</div></div>
    <div class="panel">
      <p class="product">Vitamin C</p>
      <p class="sub">Cream</p>
      <div class="row">
        <div class="badge">CBG<small>INFUSED</small></div>
        <div class="dose"><p class="line">300mg CBG</p><small>For Beauty</small><p class="claims">BRIGHTEN + HYDRATE</p></div>
      </div>
    </div>
    <p class="net-wt">NET WT .5 OZ / 15G</p>
  </section>

</body>
</html>
```